Broschüre für Immobilienvertrieb
Zielgruppe
Wir sind ein Immobilienvertrieb im Bereich Neubau-Immobilien und Bestand-Immobilien aus München. Die Firma BLOR existiert seit über 30 Jahren. Vor 4 Jahren haben wir ein cooles modernes Rebranding durchgeführt, sodass man mit unserem neuen Corporate Design richtig Spaß am Gestalten haben kann.
Eine konkrete Zielgruppe zu definieren ist schwierig, da unsere Käufer von 20-80 Jahren sein können. Ob junge, erfolgreiche Menschen, junge Familien, ältere Erwachsene, die von sich nach Auszug ihrer Kinder von ihrem Haus trennen wollen und eine kleinere Wohnung suchen oder einfach der Kapitalanleger, der auf der Suche nach einer neuen Investition ist.
Unsere CI ist gradlinig und setzt sich aus anthrazit, neonorange und weiß zusammen (Styleguide ist anbei).
Im Bestand gibt es nicht pro Objekt ein CI, hier wird mit dem der BLOR gearbeitet. Im Neubau hat jedes einzelne Projekt sein eigenes CI (siehe aktuell zeltholm.de).
www.blor.de
Aufgabenstellung
Zur Aufgabe: Für die Bestandimmobilien benötigen wir ein neues Layout eines Immobilienexposé. Das Exposé wird sowohl online verwendet als auch von uns selbst gedruckt und gebunden.
Input: beigefügt ein Beispielexposé - grundsätzlich gefällt uns das Design, wir möchten jedoch etwas NEUES, modernes. Bitte keine Kopien des alten Exposés, dies soll nur als Input dienen (gerne können die Daten der Wohnung für den neuen Designentwurf genutzt werden).
Die Datei soll von uns befüllbar sein, sodass wir Texte und Bilder selbst austauschen können.
Für die Onlinenutzung gerne als doppelseitige Datei, zum Beispiel um Bilder über zwei Seiten größer und schöner darstellen zu können (Auszug Beispielimmobilie anbei). Für den Druck wird die Datei zudem mit Einzelseiten benötigt.

```html
<!DOCTYPE html>
<html lang="de">
<head>
<meta charset="utf-8">
<title>Exposé Ahornstraße München</title>
<link rel="stylesheet" href="https://fonts.googleapis.com/css2?family=Montserrat:wght@400;500;600;700&family=Nunito+Sans:wght@400;600;700&display=swap">
<style>
  :root {
    --anthracite: #2b2d31;
    --neon-orange: #ee4f2c;
    --orange-light: #f2834f;
    --white: #ffffff;
    --backdrop: #e9e6e2;
    --map-grey: #e3e3e3;
    --text-light: #e6e6e6;
  }
  * { margin: 0; padding: 0; box-sizing: border-box; }
  html, body { width: 1200px; height: 900px; overflow: hidden; }
  body {
    background: var(--backdrop);
    font-family: "Nunito Sans", sans-serif;
    position: relative;
  }

  /* ---------- Cover ---------- */
  .cover {
    position: absolute; left: 40px; top: 190px;
    width: 370px; height: 520px;
    background: var(--anthracite);
    overflow: hidden;
  }
  .cover-photo {
    position: absolute; left: 0; top: 0; width: 100%; height: 372px;
    background: linear-gradient(160deg, #e0603a 0%, var(--orange-light) 45%, #e2673c 75%, #d9552f 100%);
  }
  .cover-frame { position: absolute; inset: 0; pointer-events: none; }
  .cover-brand {
    position: absolute; top: 62px; left: 0; width: 100%; text-align: center;
    color: var(--white);
  }
  .brand-name {
    font-family: "Montserrat", sans-serif; font-weight: 600;
    font-size: 30px; letter-spacing: 6px;
  }
  .brand-tagline {
    margin-top: 18px;
    font-family: "Montserrat", sans-serif; font-weight: 600;
    font-size: 8.5px; letter-spacing: 1.6px;
  }
  .cover-mark { position: absolute; left: 171px; top: 357px; }
  .cover-title {
    position: absolute; top: 410px; left: 0; width: 100%; text-align: center;
    color: var(--white);
    font-family: "Montserrat", sans-serif; font-weight: 600;
    font-size: 15px; letter-spacing: 2.6px; line-height: 18px;
  }
  .cover-subtitle {
    position: absolute; top: 452px; left: 0; width: 100%; text-align: center;
    color: var(--text-light);
    font-family: "Montserrat", sans-serif; font-weight: 400;
    font-size: 8px; letter-spacing: 1.2px; line-height: 10.5px;
  }
  .cover-object {
    position: absolute; left: 18px; top: 496px;
    color: var(--white);
    font-family: "Montserrat", sans-serif; font-weight: 600;
    font-size: 7px; letter-spacing: 1.4px;
  }

  /* ---------- Spread ---------- */
  .spread {
    position: absolute; left: 440px; top: 190px;
    width: 720px; height: 520px;
    display: flex;
  }
  .page { position: relative; width: 360px; height: 100%; overflow: hidden; }
  .page-left { background: var(--anthracite); display: flex; }
  .page-right { background: var(--white); }

  .text-column { position: relative; width: 186px; height: 100%; padding: 0 14px 0 17px; }
  .page-number {
    position: absolute; top: 22px;
    font-family: "Montserrat", sans-serif; font-weight: 600; font-size: 5px;
  }
  .page-left .page-number { left: 18px; color: var(--white); }
  .page-left .page-tick { position: absolute; left: 0; top: 24px; width: 12px; height: 3px; background: var(--white); }
  .page-right .page-number { right: 20px; color: var(--anthracite); }
  .page-right .page-tick { position: absolute; right: 0; top: 24px; width: 12px; height: 3px; background: var(--neon-orange); }

  .section-title {
    margin-top: 64px;
    font-family: "Montserrat", sans-serif; font-weight: 400;
    font-size: 14px; letter-spacing: 1.6px; color: var(--white);
  }
  .section-title .plus { color: var(--neon-orange); font-weight: 700; font-size: 11px; margin-right: 4px; }
  .section-title strong { color: var(--neon-orange); font-weight: 700; }

  .body-copy {
    margin-top: 18px;
    color: var(--text-light);
    font-size: 7px; line-height: 11px; letter-spacing: 0.15px;
    text-align: justify; hyphens: manual;
  }
  .body-copy p + p { margin-top: 11px; }

  .photo-panel {
    width: 174px; height: 100%;
    background: linear-gradient(180deg, #8e9fb9 0%, #b7a28a 16%, #9c8a6a 28%, #8f8a3c 45%, #6f8a3a 62%, #c9c6bc 76%, #5f7a38 100%);
  }

  .page-footer {
    position: absolute; bottom: 16px;
    font-size: 5px; letter-spacing: 0.2px; white-space: nowrap;
  }
  .page-footer strong { font-weight: 700; }
  .page-left .page-footer { left: 112px; color: var(--text-light); }
  .page-right .page-footer { left: 0; width: 100%; text-align: center; color: var(--anthracite); }

  .map-area {
    position: absolute; left: 16px; top: 35px; width: 324px; height: 446px;
    background: linear-gradient(135deg, #ececec 0%, var(--map-grey) 50%, #efefef 100%);
  }
  .map-pin {
    position: absolute; left: 157px; top: 99px;
    background: var(--white);
    padding: 10px 10px;
    box-shadow: 0 0 0 2px var(--anthracite);
  }
  .map-pin .brand-name { color: var(--anthracite); font-size: 14px; letter-spacing: 3px; }
</style>
</head>
<body>

  <section class="cover">
    <div class="cover-photo" role="img" aria-label="Orange getöntes Foto einer Hausfassade mit Balkonen, von unten fotografiert"></div>
    <svg class="cover-frame" width="370" height="520" viewBox="0 0 370 520">
      <polyline points="264,20 18,20 18,486" fill="none" stroke="#ffffff" stroke-width="2"/>
      <polyline points="351,20 351,500 108,500" fill="none" stroke="#ffffff" stroke-width="2"/>
    </svg>
    <div class="cover-brand">
      <div class="brand-name">BLOR</div>
      <div class="brand-tagline">MIT HERZ ZUM ZUHAUSE</div>
    </div>
    <svg class="cover-mark" width="28" height="30" viewBox="0 0 28 30">
      <line x1="2" y1="1" x2="26" y2="29" stroke="#ee4f2c" stroke-width="5"/>
      <line x1="26" y1="1" x2="2" y2="29" stroke="#ee4f2c" stroke-width="5"/>
    </svg>
    <h1 class="cover-title">AHORNSTRASSE<br>MÜNCHEN</h1>
    <p class="cover-subtitle">MÖBILIERTE &amp; GUT VERMIETETE KAPITALANLAGE<br>IN GUTER LAGE MIT BALKON &amp; STELLPLATZ</p>
    <p class="cover-object">OBJEKT XX - 2.OG</p>
  </section>

  <section class="spread">
    <article class="page page-left">
      <div class="text-column">
        <span class="page-tick"></span>
        <span class="page-number">8</span>
        <h2 class="section-title"><span class="plus">+</span>OBJEKT<strong>LAGE</strong></h2>
        <div class="body-copy">
          <p>Durch die zentrale Lage des Objektes be&shy;finden sich alle Ein&shy;richtungen und Ge&shy;schäfte des täglichen Be&shy;darfs in der Nähe.</p>
          <p>Das neu ent&shy;standene Stadt&shy;quartier „Nordtor“ wertet die nähere Um&shy;gebung der Wohn&shy;anlage eben&shy;falls auf. Hier be&shy;findet sich auch der nächste Super&shy;markt (Marktwerk), ein Luxus&shy;hotel, Restau&shy;rants, weitere Shopping&shy;möglich&shy;keiten mit einem viel&shy;seitigen Ange&shy;bot sowie Arzt&shy;praxen, die in ca. 200m zu Fuß schnell zu er&shy;reichen sind.</p>
          <p>An den öffent&shy;lichen Verkehr ist die Ahorn48 optimal an&shy;gebunden. Die Tram&shy;bahn&shy;station „Münchner Tor“ befindet sich direkt vor dem Haus. Von dort aus fährt die Tram&shy;linie 23 über die Park&shy;stadt Schwa&shy;bing Richtung Schwa&shy;bing Nord, oder inner&shy;halb von drei Stationen zur Münchner Freiheit. Von der haben Sie An&shy;schluss an die U-Bahn&shy;linien U3, U6, U8.</p>
          <p>Durch den Airport Express Bus (Abfahrt am Nord&shy;friedhof) erreichen Sie im 15 Minuten&shy;takt in ca. einer halben Stunde den Flug&shy;hafen München.</p>
        </div>
      </div>
      <div class="photo-panel" role="img" aria-label="Luftaufnahme: Stadtpanorama mit Alpen, herbstlicher Park und weißes Wohnhaus im Vordergrund"></div>
      <p class="page-footer"><strong>Exposé</strong> | Ahornstr. 48 | Objektnr. XX - München</p>
    </article>

    <article class="page page-right">
      <span class="page-number">9</span>
      <span class="page-tick"></span>
      <div class="map-area" role="img" aria-label="Stadtplan der Umgebung mit Straßen, Haltestellen, Restaurants und Hotels">
        <div class="map-pin"><span class="brand-name">BLOR</span></div>
      </div>
      <p class="page-footer"><strong>Exposé</strong> | Ahornstr. 48 | Objektnr. XX - München</p>
    </article>
  </section>

</body>
</html>
```